New Dental Office Needs an Attractive and user friendly Website Designed

I need a website for a new dental office. The Name is Maplecrest Dentistry. I would like a Modern design with a user friendly interface and usability.
I would like a landing page, a page that lists the services we offer: Cosmetic Dentistry, Implants, Dental Hygiene, Emergency Services, Restorations, Dentures
Target Market(s)
Mid to upper class
Industry/Entity Type
Dentistry
Coding
Coded - Design and coding required
Number of Pages Required
1 page
Requirements
Must have
- Landing page that has a scheduling option, Procedures, operating hours, and contact us info
Nice to have
- Appealing design, Soft comforting colors. Easy to navigate page, Modern and professional.

```html
<!DOCTYPE html>
<html lang="en">
<head>
<meta charset="utf-8">
<title>Maplecrest Dentistry</title>
<link rel="stylesheet" href="https://fonts.googleapis.com/css2?family=Inter:ital,wght@0,300;0,400;0,500;0,600;1,300&family=Tinos:ital,wght@0,400;1,700&display=swap">
<style>
:root{
  --ink:#171b26;
  --ink-soft:#2a2f3b;
  --paper:#ffffff;
  --canvas:#e6e7ea;
  --muted:#8a8e97;
  --line:#c9cbd0;
  --rule-dark:#3a3f4b;
  --serif:"Tinos", "Times New Roman", serif;
  --sans:"Inter", Arial, sans-serif;
}
*{margin:0;padding:0;box-sizing:border-box}
html,body{width:1200px;height:4900px;overflow:hidden}
body{background:var(--canvas);position:relative;font-family:var(--sans);color:var(--ink)}
.section{position:absolute;left:38px;width:1122px;overflow:hidden}
.abs{position:absolute}
.dark{background:var(--ink);color:#fff}
.light{background:var(--paper)}
.vline{position:absolute;left:560px;width:1px;background:#7d818b}
.circle-btn{width:34px;height:34px;border-radius:50%;display:flex;align-items:center;justify-content:center}
.circle-btn.solid{background:var(--ink)}
.circle-btn.white{background:#fff}
.circle-btn.grey{background:#8e9199}
.circle-btn.pale{background:#e3e4e7}

/* hero */
.hero{top:48px;height:700px}
.hero-photo{position:absolute;inset:0;background:linear-gradient(100deg,#2a2c30 0%,#3b3e44 40%,#6a6d72 62%,#4a4c50 80%,#2c2e31 100%)}
.hero-shade{position:absolute;left:0;top:0;width:520px;height:100%;background:linear-gradient(90deg,rgba(20,22,28,.6),rgba(20,22,28,0))}
.brand{left:44px;top:18px;color:#fff;font-family:var(--serif)}
.brand-name{font-size:21px;line-height:1}
.brand-sub{font-family:var(--sans);font-size:7px;letter-spacing:2px;margin-top:3px;padding-left:8px}
.main-nav{left:470px;top:29px;display:flex;gap:12px}
.main-nav a{color:#fff;font-size:10.5px;font-weight:600;letter-spacing:.5px;text-decoration:underline;text-underline-offset:3px}
.nav-rule{left:0;top:70px;width:100%;height:1px;background:rgba(255,255,255,.35)}
.hero-lead{left:44px;top:118px;width:420px;font-family:var(--serif);font-size:26px;line-height:40px;color:#fff}
.watch{left:44px;top:262px;display:flex;align-items:center;gap:14px;color:#fff;font-size:8.5px;letter-spacing:1px}
.hero-word{left:40px;top:490px;font-family:var(--serif);font-size:142px;line-height:1;color:rgba(235,236,238,.9);letter-spacing:1px}

/* entry points */
.entry{top:748px;height:637px}
.section-title{position:absolute;left:0;width:100%;text-align:center;font-family:var(--serif);font-size:31px;color:var(--ink)}
.entry-card{position:absolute;top:169px;width:249px}
.entry-photo{height:289px}
.entry-label{display:flex;justify-content:space-between;align-items:center;margin-top:14px;font-size:16px}

/* doctor */
.doctor{top:1385px;height:873px}
.doctor-photo{left:44px;top:141px;width:511px;height:593px;background:linear-gradient(160deg,#dfe5ea 0%,#b8c2ca 45%,#5b4a3e 70%,#1d1f24 100%)}
.doctor-title{left:656px;top:252px;font-family:var(--serif);font-size:28px;line-height:42px}
.doctor-text{left:656px;width:410px;font-family:var(--serif);font-size:13.5px;line-height:24px;color:#e2e3e6}
.text-link{display:flex;align-items:center;gap:10px;font-size:8.5px;letter-spacing:.8px}

/* reservation */
.reserve{top:2258px;height:668px}
.reserve-title{left:0;top:166px;width:100%;text-align:center;font-size:32px}
.reserve-title em{font-family:var(--serif);font-weight:700;font-style:italic}
.reserve-sub{left:0;top:203px;width:100%;text-align:center;font-size:11.5px;line-height:19px}
.field{position:absolute;width:296px;border-bottom:1px solid #6f737b;font-size:9px;letter-spacing:.8px;padding:0 0 10px 12px}
.field.date{padding-top:0}
.field.date small{display:block;font-size:8px;color:var(--muted)}
.extras-label{left:63px;top:432px;font-size:9px;letter-spacing:.8px}
.extras{left:63px;top:452px;display:flex;gap:30px;font-size:8.5px;letter-spacing:.6px}
.extras span{display:flex;align-items:center;gap:8px}
.extras i{width:9px;height:9px;border:1px solid #b9bcc2;display:inline-block}
.submit{left:760px;top:521px;width:70px;height:28px;background:var(--ink);color:#fff;font-size:9px;letter-spacing:.8px;display:flex;align-items:center;justify-content:center}

/* testimonial */
.review{top:2926px;height:700px}
.eyebrow{font-size:8px;letter-spacing:.8px;color:#c6c8cd}
.quote{left:44px;top:200px;width:900px;font-family:var(--serif);font-size:47px;line-height:56px}
.rule{height:1px;background:var(--rule-dark)}
.avatar{left:44px;top:465px;width:68px;height:78px;background:linear-gradient(180deg,#b7aca3,#4a3a33)}
.reviewer{left:132px;top:490px;font-family:var(--serif)}
.reviewer b{font-weight:400;font-size:15px;display:block}
.reviewer span{font-size:10px;color:#c6c8cd}

/* news */
.news{top:3626px;height:570px}
.news-title{left:44px;top:32px;white-space:nowrap;font-family:var(--serif);font-size:112px;line-height:1;letter-spacing:1px}
.post{position:absolute;top:179px;width:249px}
.post-photo{height:137px}
.post-title{margin-top:20px;font-family:var(--serif);font-size:12.5px;line-height:15px}
.post-meta{display:flex;justify-content:space-between;align-items:center;margin-top:12px;font-size:8.5px;letter-spacing:.6px}
.tag{background:#e3e4e7;border-radius:12px;padding:6px 12px;font-size:8px;letter-spacing:.8px}
.all-posts{left:44px;top:516px;display:flex;align-items:center;gap:10px;font-size:8.5px;letter-spacing:.8px}

/* talk + footer */
.talk{top:4196px;height:328px}
.talk-text{left:0;top:150px;width:100%;text-align:center;font-size:56px;font-weight:300;font-style:italic}
.talk-text span{border-bottom:2px solid #fff;padding:0 2px 4px}
.marks{top:4524px;height:156px;display:flex;border-top:1px solid var(--rule-dark);border-bottom:1px solid var(--rule-dark)}
.mark-cell{flex:1;display:flex;align-items:center;justify-content:center;border-right:1px solid var(--rule-dark);font-family:var(--serif);font-size:20px;color:#fff}
.mark-cell:last-child{border-right:none}
.footer{top:4680px;height:172px}
.pill{top:114px;height:38px;border-radius:19px;background:#fff;color:var(--ink);display:flex;align-items:center;gap:12px;padding:0 18px;font-size:9.5px}
.legal{left:380px;top:122px;width:360px;text-align:center;font-size:8px;line-height:12px;letter-spacing:.6px;color:#d4d6da}
.socials{left:770px;top:114px;display:flex;gap:15px}
.socials span{width:38px;height:38px;border-radius:50%;background:#fff;display:flex;align-items:center;justify-content:center}
.socials span i{width:14px;height:14px;border-radius:50%;background:var(--ink)}
</style>
</head>
<body>

<!-- Hero -->
<header class="section hero dark">
  <div class="hero-photo" role="img" aria-label="Dentist in a dark uniform treating a reclined patient with a dental microscope"></div>
  <div class="hero-shade"></div>
  <div class="abs brand"><div class="brand-name">Maplecrest</div><div class="brand-sub">— DENTISTRY —</div></div>
  <nav class="abs main-nav"><a>HOME</a><a>SERVICE</a><a>CONTACT</a></nav>
  <svg class="abs" style="left:1000px;top:30px" width="72" height="16" viewBox="0 0 72 16" fill="none" stroke="#fff" stroke-width="1.5">
    <path d="M0 4h30M0 9h30M8 14h22"/><circle cx="60" cy="7" r="5"/><path d="M64 11l4 4"/>
  </svg>
  <div class="abs nav-rule"></div>
  <p class="abs hero-lead">Because you deserve more than just a dentist. You deserve a partner in your smile journey.</p>
  <div class="abs watch">WATCH THE FULL VIDEO
    <span class="circle-btn solid"><svg width="14" height="12" viewBox="0 0 14 12" fill="none" stroke="#fff" stroke-width="1.6"><path d="M1 6h11M7 1l5 5-5 5"/></svg></span>
  </div>
  <div class="abs hero-word">MAPLECREST</div>
</header>

<!-- Entry points -->
<section class="section entry light">
  <h2 class="section-title" style="top:112px">Our main entry points</h2>
  <article class="entry-card" style="left:44px"><div class="entry-photo" role="img" aria-label="Close-up of a smile with a dental mirror" style="background:linear-gradient(135deg,#2a7fb0,#c98a7a 60%,#6b2f2a)"></div><div class="entry-label">Cosmetic Dentistry<svg width="16" height="12" viewBox="0 0 16 12" fill="none" stroke="#171b26" stroke-width="1.4"><path d="M0 6h14M9 1l5 5-5 5"/></svg></div></article>
  <article class="entry-card" style="left:306px"><div class="entry-photo" role="img" aria-label="Patient holding a dental implant model" style="background:linear-gradient(160deg,#e9e5e1,#c8a898 55%,#4a3b35)"></div><div class="entry-label">Implants<svg width="16" height="12" viewBox="0 0 16 12" fill="none" stroke="#171b26" stroke-width="1.4"><path d="M0 6h14M9 1l5 5-5 5"/></svg></div></article>
  <article class="entry-card" style="left:568px"><div class="entry-photo" role="img" aria-label="Smiling woman brushing her teeth" style="background:linear-gradient(160deg,#eeeae6,#d4b5a3 55%,#6b4d3e)"></div><div class="entry-label">Dental Hygiene<svg width="16" height="12" viewBox="0 0 16 12" fill="none" stroke="#171b26" stroke-width="1.4"><path d="M0 6h14M9 1l5 5-5 5"/></svg></div></article>
  <article class="entry-card" style="left:829px"><div class="entry-photo" role="img" aria-label="Dentist examining a patient in a treatment chair" style="background:linear-gradient(160deg,#e2e4e6,#a9adb2 55%,#3a3d42)"></div><div class="entry-label">Emergency Services<svg width="16" height="12" viewBox="0 0 16 12" fill="none" stroke="#171b26" stroke-width="1.4"><path d="M0 6h14M9 1l5 5-5 5"/></svg></div></article>
  <span class="abs circle-btn grey" style="left:984px;top:544px"><svg width="14" height="12" viewBox="0 0 14 12" fill="none" stroke="#fff" stroke-width="1.6"><path d="M13 6H2M7 1L2 6l5 5"/></svg></span>
  <span class="abs circle-btn solid" style="left:1039px;top:544px"><svg width="14" height="12" viewBox="0 0 14 12" fill="none" stroke="#fff" stroke-width="1.6"><path d="M1 6h11M7 1l5 5-5 5"/></svg></span>
  <div class="vline" style="top:541px;height:96px"></div>
</section>

<!-- Doctor -->
<section class="section doctor dark">
  <div class="vline" style="top:0;height:95px"></div>
  <div class="abs doctor-photo" role="img" aria-label="Portrait of the head dentist in a dark blazer"></div>
  <h2 class="abs doctor-title" style="font-weight:400">Meet our Head<br>Dr. Elena Hart</h2>
  <p class="abs doctor-text" style="top:361px">At Dr. Elena Hart’s office, we combine years of experience with cutting-edge technology to provide exceptional dental care tailored just for you. Our mission is simple: to make you comfortable, confident, and proud of your smile.results with minimal discomfort.</p>
  <p class="abs doctor-text" style="top:509px">Discover a dental experience where advanced technology meets compassionate care — because your smile deserves nothing less.</p>
  <div class="abs text-link" style="left:656px;top:602px">LEARN MORE ABOUT ELENA HART
    <span class="circle-btn white"><svg width="14" height="12" viewBox="0 0 14 12" fill="none" stroke="#171b26" stroke-width="1.6"><path d="M1 6h11M7 1l5 5-5 5"/></svg></span>
  </div>
  <div class="vline" style="top:780px;height:93px"></div>
</section>

<!-- Reservation -->
<section class="section reserve light">
  <div class="vline" style="top:0;height:92px"></div>
  <h2 class="abs reserve-title" style="font-weight:400">Reservation <em>enquiry</em></h2>
  <p class="abs reserve-sub">We eagerly await your contact and look forward to welcoming you<br>soon for an unforgettable and luxurious experience.</p>
  <div class="field" style="left:63px;top:274px">BOOKER</div>
  <div class="field" style="left:412px;top:274px">FIRST NAME</div>
  <div class="field" style="left:760px;top:274px">LAST NAME</div>
  <div class="field" style="left:63px;top:358px">PHONE NUMBER</div>
  <div class="field" style="left:412px;top:358px">E-MAIL</div>
  <div class="field date" style="left:760px;top:352px"><small>DATE</small>MM/DD/YYYY</div>
  <div class="abs extras-label">ADDITIONALS:</div>
  <div class="abs extras"><span><i></i>COSMETIC DENTISTRY</span><span><i></i>IMPLANTS</span><span><i></i>DENTAL HYGIENE</span><span><i></i>EMERGENCY SERVICES</span><span><i></i>RESTORATIONS</span><span><i></i>DENTURES</span></div>
  <div class="field" style="left:63px;top:510px;width:645px;padding-bottom:28px">YOUR MESSAGE</div>
  <div class="abs submit">SUBMIT</div>
  <div class="vline" style="top:620px;height:48px"></div>
</section>

<!-- Testimonial -->
<section class="section review dark">
  <div class="vline" style="top:0;height:93px"></div>
  <div class="abs eyebrow" style="left:44px;top:164px">MAPLECREST DENTISTRY</div>
  <span class="abs circle-btn pale" style="left:993px;top:146px"><svg width="14" height="12" viewBox="0 0 14 12" fill="none" stroke="#171b26" stroke-width="1.6"><path d="M13 6H2M7 1L2 6l5 5"/></svg></span>
  <span class="abs circle-btn white" style="left:1041px;top:146px"><svg width="14" height="12" viewBox="0 0 14 12" fill="none" stroke="#171b26" stroke-width="1.6"><path d="M1 6h11M7 1l5 5-5 5"/></svg></span>
  <blockquote class="abs quote">“Dr. Hart made me feel comfortable from day one. The care and professionalism are unmatched. I love my smile now!”</blockquote>
  <div class="abs rule" style="left:44px;top:449px;width:858px"></div>
  <div class="abs avatar" role="img" aria-label="Portrait of the patient"></div>
  <div class="abs reviewer"><b>Naomi L.</b><span>Patient</span></div>
  <div class="abs rule" style="left:44px;top:560px;width:858px"></div>
  <div class="vline" style="top:607px;height:93px"></div>
</section>

<!-- News -->
<section class="section news light">
  <h2 class="abs news-title" style="font-weight:400">LATEST NEWS + BLOG</h2>
  <article class="post" style="left:44px"><div class="post-photo" role="img" aria-label="Dentist wearing a mask and loupes" style="background:linear-gradient(135deg,#1f3f5c,#5d89a8 55%,#1a2330)"></div><h3 class="post-title" style="font-weight:400">Smile Like You Mean It:<br>7 Secrets to a Healthier,<br>Whiter Smile</h3><div class="post-meta" style="margin-top:26px"><span class="tag">PERFORMING ARTS</span><span>16 MAY 2025</span></div></article>
  <article class="post" style="left:306px"><div class="post-photo" role="img" aria-label="Dental model of a jaw" style="background:linear-gradient(135deg,#d8b99a,#e9d6c8 50%,#9b5e4b)"></div><h3 class="post-title" style="font-weight:400">Don’t Skip the Dentist:<br>What Really Happens When<br>You Put Off That Appointment</h3><div class="post-meta"><span class="tag">PREP</span><span>15 MAY 2025</span></div></article>
  <article class="post" style="left:568px"><div class="post-photo" role="img" aria-label="Close-up of a bright smile" style="background:linear-gradient(135deg,#a8433d,#e7b1a3 55%,#7a2d29)"></div><h3 class="post-title" style="font-weight:400">Coffee, Wine &amp; Your Teeth:<br>How to Keep Your Smile Bright<br>Without Giving Up What You Love</h3><div class="post-meta"><span class="tag">MUSIC</span><span>15 MAY 2025</span></div></article>
  <article class="post" style="left:829px"><div class="post-photo" role="img" aria-label="Dentist in a white coat in a clinic" style="background:linear-gradient(135deg,#c9c2b5,#e7e3dc 50%,#6e6a63)"></div><h3 class="post-title" style="font-weight:400">No Judgement, Just Solutions:<br>Why It’s Never Too Late to Fix<br>Your Smile</h3><div class="post-meta"><span class="tag">PERFORMING ARTS</span><span>14 MAY 2025</span></div></article>
  <article class="post" style="left:1091px"><div class="post-photo" role="img" aria-label="Dental clinic interior" style="background:linear-gradient(135deg,#6d7e8f,#a8b4bf)"></div><h3 class="post-title" style="font-weight:400">From<br>How<br>in To</h3><div class="post-meta"><span class="tag">BRI</span></div></article>
  <div class="abs all-posts">ALL POSTS
    <span class="circle-btn solid" style="width:38px;height:38px"><svg width="14" height="12" viewBox="0 0 14 12" fill="none" stroke="#fff" stroke-width="1.6"><path d="M1 6h11M7 1l5 5-5 5"/></svg></span>
  </div>
  <span class="abs circle-btn pale" style="left:993px;top:518px"><svg width="14" height="12" viewBox="0 0 14 12" fill="none" stroke="#a4a7ad" stroke-width="1.6"><path d="M13 6H2M7 1L2 6l5 5"/></svg></span>
  <span class="abs circle-btn pale" style="left:1041px;top:518px"><svg width="14" height="12" viewBox="0 0 14 12" fill="none" stroke="#171b26" stroke-width="1.6"><path d="M1 6h11M7 1l5 5-5 5"/></svg></span>
</section>

<!-- Let's talk -->
<section class="section talk dark">
  <div class="vline" style="top:0;height:95px"></div>
  <div class="abs talk-text"><span>Let’s talk</span></div>
  <div class="vline" style="top:236px;height:92px"></div>
</section>

<div class="section marks dark">
  <div class="mark-cell">Maplecrest</div><div class="mark-cell">Maplecrest</div><div class="mark-cell">Maplecrest</div><div class="mark-cell">Maplecrest</div><div class="mark-cell">Maplecrest</div><div class="mark-cell">Maplecrest</div><div class="mark-cell">Maplecrest</div>
</div>

<footer class="section footer dark">
  <div class="abs pill" style="left:38px;width:200px">
    <svg width="14" height="11" viewBox="0 0 14 11" fill="none" stroke="#171b26" stroke-width="1.3"><rect x=".7" y=".7" width="12.6" height="9.6" rx="1.5"/><path d="M1 1.5l6 4.5 6-4.5"/></svg>hello@maplecrest.example</div>
  <div class="abs pill" style="left:249px;width:155px">
    <svg width="13" height="13" viewBox="0 0 13 13" fill="none" stroke="#171b26" stroke-width="1.3"><path d="M3 1l2 3-1.3 1.3a7 7 0 0 0 4 4L9 8l3 2-1 2C6 12 1 7 1 2z"/></svg>+1 555 014 7290</div>
  <div class="abs legal">© 2025 MAPLECREST DENTISTRY<br>ALL RIGHTS RESERVED</div>
  <div class="abs socials"><span><i></i></span><span><i></i></span><span><i></i></span><span><i></i></span><span><i></i></span></div>
</footer>

</body>
</html>
```